Fishing charter business in Sitka Alaska needs new business card design

I have had the same design for 10 plus years, ready for something different. I have attached a copy of my current card and my website link is www.tidecrestangling.example
I am looking for something that will catch my clients eye, although I rely on word of mouth for most of my business a a nice business card will help people remember who I am. My business is located in Sitka Alaska, there are probably 20-30 other charter businesses in Sitka. I like the way my current card is laid out, with the two tone black and grey. I can leave it up to the designers to come up with something else.
Target Market(s)
men, women, couples. Anyone who likes fishing
Industry/Entity Type
Tourism
Contact Information for Business Card
Dorvane's Charter Service
Kelpline Bay Sportfishing
Colors
Designer to choose colors to be used in the design.
Requirements
Must have
- Lyle Dorvane
- PO Box 4716
- Sitka, AK 99835
- Compass Rose image
- 100 Ton USCG Licensed Captain
- ldorvane@wavenet.example
- 907-555-0148
- www.tidecrestangling.example
Nice to have
- ghost image of "boat helm"
Should not have
- be to complex

```html
<!DOCTYPE html>
<html lang="en">
<head>
<meta charset="utf-8">
<title>Dorvane's Charter Service – Business Card</title>
<link rel="stylesheet" href="https://fonts.googleapis.com/css2?family=Josefin+Slab:wght@400;600&family=Cormorant+Garamond:wght@700&display=swap">
<style>
  :root {
    --sand: #ebe3dd;
    --navy: #1b2745;
    --paper: #ffffff;
    --ghost: #f5f3f0;
    --ink: #1b2745;
  }
  * { margin: 0; padding: 0; box-sizing: border-box; }
  html, body {
    width: 834px; height: 1200px; overflow: hidden;
    background: var(--paper);
  }
  .card {
    position: relative;
    width: 834px; height: 1200px;
    background: var(--paper);
    font-family: "Josefin Slab", serif;
    color: var(--ink);
    overflow: hidden;
  }
  .card__top {
    position: absolute; left: 0; top: 0;
    width: 100%; height: 424px;
    background: var(--sand);
  }
  .compass {
    position: absolute; left: 0; top: 0; width: 100%; height: 424px;
  }
  .compass__point {
    position: absolute;
    font-family: "Cormorant Garamond", serif;
    font-weight: 700;
    font-size: 30px;
    color: var(--navy);
    line-height: 1;
    transform: translate(-50%, -50%);
  }
  .compass__rose {
    position: absolute; left: 285px; top: 90px;
    width: 270px; height: 270px;
  }
  .band {
    position: absolute; left: 0; top: 424px;
    width: 100%; height: 120px;
    background: var(--navy);
    color: var(--paper);
    text-align: center;
  }
  .band__title {
    position: absolute; left: 0; right: 0; top: 16px;
    font-size: 52px; font-weight: 400; letter-spacing: 1px;
    line-height: 1;
  }
  .band__tagline {
    position: absolute; left: 0; right: 0; top: 76px;
    font-size: 30px; font-weight: 400; letter-spacing: 0.5px;
    line-height: 1;
  }
  .helm-ghost {
    position: absolute; left: 70px; top: 560px;
    width: 700px; height: 640px;
  }
  .identity {
    position: absolute; left: 0; right: 0; top: 658px;
    text-align: center;
  }
  .identity__name {
    font-size: 46px; font-weight: 400; letter-spacing: 4px; line-height: 1;
  }
  .identity__role {
    margin-top: 20px;
    font-size: 20px; font-weight: 600; line-height: 1;
  }
  .contact {
    position: absolute; left: 232px; top: 862px;
    font-size: 23px; font-weight: 400; letter-spacing: 2.5px; line-height: 1;
    list-style: none;
  }
  .contact li { height: 31px; }
  .contact li.gap { margin-top: 10px; }
  .website {
    position: absolute; left: 0; right: 0; top: 1074px;
    text-align: center;
    font-size: 22px; font-weight: 600; letter-spacing: 0.3px; line-height: 1;
  }
</style>
</head>
<body>
<main class="card">
  <section class="card__top">
    <div class="compass">
      <span class="compass__point" style="left:420px; top:70px;">N</span>
      <span class="compass__point" style="left:420px; top:390px;">S</span>
      <span class="compass__point" style="left:247px; top:226px;">W</span>
      <span class="compass__point" style="left:593px; top:226px;">E</span>
      <svg class="compass__rose" viewBox="0 0 270 270" role="img" aria-label="Compass rose emblem in navy">
        <defs>
          <radialGradient id="rose-tone" cx="50%" cy="50%" r="50%">
            <stop offset="0%" stop-color="#1b2745"/>
            <stop offset="55%" stop-color="#1b2745" stop-opacity="0.85"/>
            <stop offset="100%" stop-color="#1b2745" stop-opacity="0"/>
          </radialGradient>
        </defs>
        <circle cx="135" cy="135" r="130" fill="url(#rose-tone)"/>
      </svg>
    </div>
  </section>

  <header class="band">
    <h1 class="band__title">Dorvane's Charter Service</h1>
    <p class="band__tagline">Kelpline Bay Sportfishing</p>
  </header>

  <svg class="helm-ghost" viewBox="0 0 700 640" role="img" aria-label="Faint ghost image of a boat helm wheel">
    <defs>
      <radialGradient id="helm-tone" cx="50%" cy="48%" r="50%">
        <stop offset="0%" stop-color="#f5f3f0" stop-opacity="0.6"/>
        <stop offset="70%" stop-color="#f5f3f0"/>
        <stop offset="100%" stop-color="#f5f3f0" stop-opacity="0"/>
      </radialGradient>
    </defs>
    <circle cx="350" cy="306" r="320" fill="url(#helm-tone)"/>
  </svg>

  <section class="identity">
    <h2 class="identity__name">Lyle Dorvane</h2>
    <p class="identity__role">100 Ton USCG Licensed Captain</p>
  </section>

  <ul class="contact">
    <li>PO Box 4716</li>
    <li>Sitka, AK 99835</li>
    <li class="gap">907-555-0148</li>
    <li>ldorvane@wavenet.example</li>
  </ul>

  <p class="website">www.tidecrestangling.example</p>
</main>
</body>
</html>
```